Website design for Tallow Ridge Shipping Inc

We are looking to build a website for our company. We are a scrap metal recycling company based out of Los Angeles. We purchase scrap metal in the US and ship them to China for recycling into fresh metal ores to supply industrial users. We would designs that emphasize the color green given our name and the nature of our business. Recycling themes are welcomed. We already have a URL at:
http://tallowridgeshippinginc.com/
At this point, I would like 4 pages:
- Home page
- About Us
- Resources
- Contact us
Our sister company is Pearl Harbourline Intl Inc and they have a website that we can use as a starting point.
http://www.pearlharbourline-intl.com/
Our competitor has a website below. However we dislike the design given we believe it looks rather dull.
http://www.vastoreloop.com/en/
Lastly, this is for a website shell only. Please design the template, graphics, and color schemes. We will write the contents later.

```html
<!DOCTYPE html>
<html lang="en">
<head>
<meta charset="utf-8">
<title>Tallow Ridge Shipping – Home</title>
<link href="https://fonts.googleapis.com/css2?family=Oswald:wght@400;500&display=swap" rel="stylesheet">
<style>
  :root {
    --green: #5e9a1f;
    --green-dark: #4a8217;
    --yellow: #f6b400;
    --ink: #333333;
    --body-text: #5a5a5a;
    --muted: #9a9a9a;
    --white: #ffffff;
  }
  * { box-sizing: border-box; margin: 0; padding: 0; }
  html, body { width: 1200px; height: 800px; overflow: hidden; background: var(--white); }
  body { position: relative; font-family: Arial, Helvetica, sans-serif; }

  .site-header { position: absolute; top: 0; left: 0; width: 1200px; height: 93px; background: var(--white); }
  .brand { position: absolute; left: 120px; top: 32px; display: flex; align-items: center; gap: 10px; }
  .brand-mark { width: 26px; height: 26px; border-radius: 50%; background: var(--green); }
  .brand-name { font-family: 'Oswald', sans-serif; font-weight: 500; font-size: 20px; color: var(--green); }

  .main-nav { position: absolute; left: 428px; top: 27px; width: 650px; height: 40px; border-radius: 20px;
    background: linear-gradient(#6fae2a, var(--green-dark)); box-shadow: 0 2px 2px rgba(0,0,0,.25); display: flex; align-items: center; }
  .main-nav a { font-family: 'Oswald', sans-serif; font-size: 13px; color: var(--white); text-decoration: none; height: 40px; line-height: 40px; padding: 0 26px; }
  .main-nav a.is-active { background: linear-gradient(#ffc81a, #f0a800); border-radius: 20px 0 0 20px; width: 79px; padding: 0; text-align: center; }
  .search-field { position: absolute; right: 5px; top: 4px; width: 228px; height: 32px; border-radius: 16px; background: var(--white); box-shadow: inset 0 1px 3px rgba(0,0,0,.3); }
  .search-field svg { position: absolute; right: 14px; top: 9px; }

  .hero { position: absolute; top: 93px; left: 0; width: 1200px; height: 500px;
    background: linear-gradient(180deg, #dfe3ea 0%, #9aa3b0 4%, #4e5866 16%, #5a6472 45%, #7b8592 75%, #8f98a4 100%); }
  .hero-title { position: absolute; left: 122px; top: 105px; width: 460px; font-family: 'Oswald', sans-serif; font-weight: 500; font-size: 31px; line-height: 35px; letter-spacing: -1px; text-transform: uppercase; color: var(--green);
    text-shadow: 2px 0 0 #fff, -2px 0 0 #fff, 0 2px 0 #fff, 0 -2px 0 #fff, 1px 1px 0 #fff, -1px -1px 0 #fff, 1px -1px 0 #fff, -1px 1px 0 #fff; }
  .hero-title .highlight { color: var(--yellow); }
  .slider-dots { position: absolute; left: 130px; top: 288px; display: flex; gap: 7px; }
  .slider-dots span { width: 14px; height: 14px; border-radius: 50%; background: #3a3a3a; border: 1px solid #222; }
  .slider-dots span.is-current { background: var(--yellow); }

  .panel { position: absolute; top: 448px; background: var(--white); box-shadow: 0 1px 4px rgba(0,0,0,.25); }
  .panel h2 { font-family: 'Oswald', sans-serif; font-weight: 400; font-size: 20px; color: var(--ink); text-transform: uppercase; letter-spacing: -0.4px; }
  .panel h2 em { font-style: normal; color: var(--green); }
  .panel p { font-size: 12.5px; line-height: 18px; color: var(--body-text); text-align: justify; }
  .welcome { left: 119px; width: 630px; height: 280px; }
  .welcome h2 { position: absolute; left: 13px; top: 11px; }
  .welcome .photo { position: absolute; left: 12px; top: 53px; width: 278px; height: 213px;
    background: linear-gradient(180deg, #9fb5cf 0%, #a7a9ad 35%, #5d6a55 70%, #8a7a65 100%); }
  .welcome .copy { position: absolute; left: 303px; top: 53px; width: 315px; }
  .welcome .copy p + p { margin-top: 18px; }
  .resources { left: 780px; width: 300px; height: 280px; }
  .resources h2 { position: absolute; left: 12px; top: 11px; }
  .resources .photo { position: absolute; left: 11px; top: 53px; width: 278px; height: 120px;
    background: linear-gradient(160deg, #8fb0cf 0%, #c9a533 35%, #7d7d80 65%, #3b3b3d 100%); }
  .resources p { position: absolute; left: 12px; top: 181px; width: 277px; }

  .site-footer { position: absolute; top: 756px; left: 120px; width: 960px; height: 28px; }
  .copyright { position: absolute; left: 0; top: 5px; font-size: 12px; color: var(--muted); }
  .social { position: absolute; right: 0; top: 0; display: flex; gap: 7px; }
  .social span { width: 28px; height: 28px; display: block; }
</style>
</head>
<body>
  <header class="site-header">
    <div class="brand"><span class="brand-mark"></span><span class="brand-name">TALLOW RIDGE SHIPPING</span></div>
    <nav class="main-nav">
      <a href="#" class="is-active">HOME</a>
      <a href="#">ABOUT US</a>
      <a href="#">RESOURCES</a>
      <a href="#">CONTACT US</a>
      <div class="search-field">
        <svg width="14" height="14" viewBox="0 0 14 14"><circle cx="5.5" cy="5.5" r="4" fill="none" stroke="#aaa" stroke-width="1.6"/><line x1="8.5" y1="8.5" x2="13" y2="13" stroke="#aaa" stroke-width="2"/></svg>
      </div>
    </nav>
  </header>

  <section class="hero" role="img" aria-label="Container ship loaded with cargo containers sailing across the open sea">
    <h1 class="hero-title"><span class="highlight">We purchase scrap metal</span> in the<br>US and ship them to China for re-<br>cycling into fresh metal ores to<br>supply industrial users</h1>
    <div class="slider-dots"><span class="is-current"></span><span></span><span></span></div>
  </section>

  <article class="panel welcome">
    <h2>Welcome to <em>Tallow Ridge Shipping</em></h2>
    <div class="photo" role="img" aria-label="Los Angeles skyline with mountains behind"></div>
    <div class="copy">
      <p>We are a scrap metal recycling company based out of Los Angeles. We purchase scrap metal in the US and ship them to China for recycling into fresh metal ores to supply industrial users</p>
      <p>We are a scrap metal recycling company based out of Los Angeles. We purchase scrap metal in the US and ship them to China for recycling into fresh metal ores to supply industrial usersWe are a scrap metal recycling company based out of Los Angeles. We purchase scrap metal in the US and ship them to China for recy-cling into fresh metal ores to supply industrial users</p>
    </div>
  </article>

  <aside class="panel resources">
    <h2>Our <em>Resources</em></h2>
    <div class="photo" role="img" aria-label="Yellow excavator grabbing a pile of scrap metal"></div>
    <p>We are a scrap metal recycling company based out of Los Angeles. We purchase scrap metal in the US and ship them to China for recycling into fresh metal ores to supply industrial usersrecy-cling into fresh metal ores to supply</p>
  </aside>

  <footer class="site-footer">
    <p class="copyright">© 2013 Tallow Ridge Shipping | All Rights Reserved.</p>
    <div class="social">
      <span role="img" aria-label="Social link" style="background:#3b5998"></span>
      <span role="img" aria-label="Social link" style="background:#2aa3e0"></span>
      <span role="img" aria-label="Feed link" style="background:#f4a024"></span>
      <span role="img" aria-label="Video link" style="background:#e01b1b"></span>
      <span role="img" aria-label="Social link" style="background:#2b2b2b"></span>
    </div>
  </footer>
</body>
</html>
```